Property Management Company Business Cards

Need business cards for a property management company located in Michigan. We manage houses for clients all over the world. Young and modern company, looking for eye catching design. Please work with the attached logo.

Industry/Entity Type

Property Management

Requirements
Must have
• Need lines for address, telephone number, fax number, web site.

Also lines for name, and job title

```html
<!DOCTYPE html>
<html lang="en">
<head>
<meta charset="utf-8">
<title>Crestline Global Management – Business Cards</title>
<link rel="stylesheet" href="https://fonts.googleapis.com/css2?family=Open+Sans:wght@400;600;700;800&display=swap">
<style>
  :root {
    --sky: #00a9e8;
    --sky-soft: #2bb9ee;
    --ink: #2e2f33;
    --ink-soft: #5b5e66;
    --paper: #ffffff;
    --paper-shade: #f3f4f6;
    --backdrop: #ecedf1;
  }
  * { box-sizing: border-box; margin: 0; padding: 0; }
  html, body {
    width: 1200px; height: 900px; overflow: hidden;
    background: var(--backdrop);
    font-family: "Open Sans", Arial, sans-serif;
  }
  .card-set {
    position: absolute; inset: 0;
    display: flex; align-items: center; justify-content: center; gap: 60px;
  }
  .card {
    position: relative;
    width: 525px; height: 300px;
    border-radius: 22px;
    overflow: hidden;
    box-shadow: 0 14px 30px rgba(40, 50, 70, 0.16);
  }

  /* Brand name block */
  .brand { display: flex; align-items: center; gap: 12px; }
  .brand-dot {
    width: 38px; height: 38px; border-radius: 50%;
    background: var(--sky); flex: none;
  }
  .brand-name {
    font-weight: 800; font-size: 22px; line-height: 1.05;
    letter-spacing: 0.5px; text-transform: uppercase; color: var(--ink);
  }

  /* Front card */
  .card-front { background: linear-gradient(180deg, var(--paper) 0%, var(--paper-shade) 100%); }
  .card-front .brand { position: absolute; left: 28px; top: 24px; }
  .name-band {
    position: absolute; left: 0; right: 0; top: 98px; height: 74px;
    background: var(--sky);
    padding: 10px 28px;
  }
  .person-name { color: var(--paper); font-weight: 700; font-size: 26px; line-height: 1.15; }
  .person-title { color: var(--paper); font-weight: 400; font-size: 14px; opacity: 0.9; }
  .contact-list {
    position: absolute; left: 28px; top: 190px;
    list-style: none; display: grid; gap: 3px;
  }
  .contact-list li, .address {
    display: flex; align-items: center; gap: 8px;
    font-size: 13px; color: var(--ink-soft);
  }
  .contact-list svg, .address svg { width: 12px; height: 12px; fill: var(--ink); flex: none; }
  .address { position: absolute; right: 26px; bottom: 20px; }

  /* Back card */
  .card-back { background: var(--sky); }
  .card-back .brand {
    position: absolute; left: 50%; top: 42%; transform: translate(-50%, -50%);
  }
  .card-back .brand-dot { background: var(--ink); width: 46px; height: 46px; }
  .card-back .brand-name { font-size: 28px; }
  .back-web {
    position: absolute; left: 0; right: 0; bottom: 48px;
    text-align: center; color: var(--paper); font-size: 15px; letter-spacing: 0.3px;
  }
</style>
</head>
<body>
<main class="card-set">

  <section class="card card-front" aria-label="Business card front">
    <div class="brand">
      <span class="brand-dot"></span>
      <span class="brand-name">Crestline Global<br>Management</span>
    </div>

    <div class="name-band">
      <p class="person-name">Daniel Okafor</p>
      <p class="person-title">Managing Director</p>
    </div>

    <ul class="contact-list">
      <li>
        <svg viewBox="0 0 12 12" aria-hidden="true"><path d="M2.5 1l2 2.2-1 1.3a6 6 0 0 0 4 4l1.3-1 2.2 2-1.2 1.5C5.5 11 1 6.5 1 2.2z"/></svg>
        xxx-xxx-xxxx
      </li>
      <li>
        <svg viewBox="0 0 12 12" aria-hidden="true"><rect x="3" y="1" width="6" height="3"/><rect x="1" y="4.5" width="10" height="4.5" rx="1"/><rect x="3" y="8" width="6" height="3"/></svg>
        xxx-xxx-xxxx
      </li>
      <li>
        <svg viewBox="0 0 12 12" aria-hidden="true"><path d="M1 2.5h10v7H1z M1.5 3l4.5 3.5L10.5 3" stroke="#fff" stroke-width="0.8"/></svg>
        info@crestlineglobal.com
      </li>
      <li>
        <svg viewBox="0 0 12 12" aria-hidden="true"><circle cx="6" cy="6" r="5"/><path d="M1 6h10M6 1c-2.5 3-2.5 7 0 10M6 1c2.5 3 2.5 7 0 10" stroke="#fff" stroke-width="0.7" fill="none"/></svg>
        www.crestlineglobal.com
      </li>
    </ul>

    <p class="address">
      <svg viewBox="0 0 12 12" aria-hidden="true"><path d="M6 1l5 4.5H9.5V11h-2.5V8H5v3H2.5V5.5H1z"/></svg>
      xxxx Birchway Dr, Suite 102
    </p>
  </section>

  <section class="card card-back" aria-label="Business card back">
    <div class="brand">
      <span class="brand-dot"></span>
      <span class="brand-name">Crestline Global<br>Management</span>
    </div>
    <p class="back-web">www.crestlineglobal.com</p>
  </section>

</main>
</body>
</html>
```